I need a audit of my current site.. with suggestions and actions

My current site, www.brickwisely does not support the high tech industry we are in. I am seeking knowledge, direction and action, I will pay hourly or by job. I also need SEO help, driven with impact trusted deliverable, our clients have to trust us to do our job. We are like Vorlin to the construction industry, gathering their data for the lifecycle. Eliminating litigation, un wanted change orders and providing audit ready projects. Eveyone wins

Target Market(s)

Construction industry, Federal and Private

Industry/Entity Type

Construction industry, globally

Coding

Coded - Design and coding required

Number of Pages Required

5+ page

Font styles to use
Sans Serif

Colors
EE7325
F08F49
F5BC92
FAE3D3
FDF4ED

Requirements
Must have
• High tech look
Should not have
• Misspelled words

```html
<!DOCTYPE html>
<html lang="en">
<head>
<meta charset="utf-8">
<title>BrickWisely — Construction Technology</title>
<link href="https://fonts.googleapis.com/css2?family=Archivo+Black&family=Poppins:wght@400;500;600;700;800&display=swap" rel="stylesheet">
<style>
:root{
  --orange:#f5a11c;
  --orange-deep:#ec6a24;
  --brand:#ee7325;
  --peach:#f5bc92;
  --blush:#fae3d3;
  --cream:#fdf4ed;
  --navy:#0a1430;
  --navy-2:#13204a;
  --ink:#1b1b1b;
  --text:#4a4a4a;
  --blue:#1a96d4;
  --grey-card:#b7b7b7;
  --white:#ffffff;
}
*{margin:0;padding:0;box-sizing:border-box}
html,body{width:1200px;height:4717px;overflow:hidden}
body{position:relative;background:var(--white);font-family:"Poppins",sans-serif;color:var(--text)}
.abs{position:absolute}
.display{font-family:"Archivo Black","Poppins",sans-serif}
.heavy{font-weight:800;text-transform:uppercase;letter-spacing:.5px}

/* top bar */
.topbar{left:0;top:0;width:1200px;height:33px;background:var(--navy);color:var(--white);font-size:13px;display:flex;align-items:center;padding:0 92px}
.topbar .dot{width:20px;height:20px;border-radius:50%;background:var(--orange);display:inline-flex;align-items:center;justify-content:center;margin-right:10px}
.topbar .addr{position:absolute;left:640px;display:flex;align-items:center}
.login{position:absolute;right:93px;top:5px;width:59px;height:23px;background:var(--orange);color:var(--navy);font-size:12px;font-weight:600;display:flex;align-items:center;justify-content:center}

/* header */
.logo{display:flex;align-items:center;gap:8px;font-weight:500;color:#8a8a8a;font-size:30px;letter-spacing:-.5px}
.logo .mark{width:14px;height:14px;background:var(--orange)}
.nav{left:465px;top:60px;display:flex;gap:23px;font-size:15px;color:var(--ink)}
.phone{left:949px;top:56px;display:flex;align-items:center;gap:10px;font-size:15px;color:var(--ink)}
.phone .dot{width:32px;height:32px;border-radius:50%;background:var(--orange);display:flex;align-items:center;justify-content:center}

/* hero */
.hero-visual{left:0;top:110px;width:1200px;height:590px;
  background:
    radial-gradient(ellipse 260px 300px at 960px 300px,rgba(120,70,40,.45),rgba(120,70,40,0) 70%),
    radial-gradient(ellipse 220px 120px at 900px 170px,rgba(255,255,255,.7),rgba(255,255,255,0) 70%),
    radial-gradient(ellipse 300px 220px at 760px 470px,rgba(190,95,45,.45),rgba(190,95,45,0) 70%),
    linear-gradient(90deg,#ffffff 0%,#fffaf6 30%,#fae3d3 48%,#f5bc92 62%,#f08f49 80%,#ee7325 100%)}
.hero-kicker{left:88px;top:198px;font-size:23px;font-weight:800;color:var(--ink);letter-spacing:.5px}
.hero-title{left:86px;top:228px;font-size:63px;line-height:70px;color:var(--ink)}
.hero-list{left:92px;top:380px;list-style:none;font-size:15px;color:var(--ink);line-height:25.7px}
.hero-list li{display:flex;align-items:center;gap:12px}
.btn-orange{left:92px;top:528px;width:181px;height:55px;background:var(--orange);color:var(--white);font-size:15px;font-weight:600;display:flex;align-items:center;justify-content:center}
.dots{display:flex;gap:8px}
.dots i{width:9px;height:9px;border-radius:50%;border:1px solid #aaa;display:block}
.dots i.on{background:var(--orange);border-color:var(--orange)}

/* about */
.hex-wrap{position:absolute;filter:drop-shadow(0 4px 8px rgba(0,0,0,.22))}
.hex{width:100%;height:100%;clip-path:polygon(50% 0,100% 25%,100% 75%,50% 100%,0 75%,0 25%);background:var(--white);position:relative}
.hex .photo{position:absolute;inset:9px;clip-path:polygon(50% 0,100% 25%,100% 75%,50% 100%,0 75%,0 25%)}
.person{font-size:14px;color:var(--ink);line-height:20px;font-weight:700}
.person span{font-weight:500;color:#555}
.about-title{left:599px;top:850px;font-size:32px;font-weight:800;color:var(--ink)}
.about-text{left:599px;width:500px;font-size:14.5px;line-height:25.7px;color:#555;letter-spacing:.3px}
.btn-dark{background:var(--ink);color:var(--white);font-size:15px;font-weight:600;display:flex;align-items:center;justify-content:center;text-transform:uppercase}

/* why */
.why-visual{left:0;top:1343px;width:1200px;height:410px;
  background:
    radial-gradient(ellipse 140px 90px at 290px 1480px,rgba(214,170,40,.55),rgba(214,170,40,0) 70%),
    radial-gradient(ellipse 130px 80px at 545px 1455px,rgba(230,230,225,.55),rgba(230,230,225,0) 70%),
    radial-gradient(ellipse 260px 200px at 420px 1640px,rgba(120,100,70,.45),rgba(120,100,70,0) 70%),
    linear-gradient(100deg,#545a61 0%,#3a3f45 45%,#2a2e33 100%);
  background-attachment:local}
.why-panel{left:0;top:1420px;width:1200px;height:302px;background:var(--blue);clip-path:polygon(733px 0,1200px 0,1200px 302px,531px 302px)}
.why-title{right:81px;top:1515px;text-align:right;font-size:33px;line-height:47px;color:var(--white)}

/* features */
.features{left:0;top:1753px;width:1200px;height:570px;background:linear-gradient(180deg,#e9e9e9 0%,#f7f7f7 60%,#ececec 100%)}
.ribbon{position:absolute;height:64px;color:var(--white);font-size:16px;font-weight:700;text-transform:uppercase;display:flex;align-items:center;line-height:20px;letter-spacing:.4px}
.ribbon.left{clip-path:polygon(0 0,100% 0,86% 100%,0 100%);justify-content:center;padding-right:40px;text-align:center}
.ribbon.right{clip-path:polygon(14% 0,100% 0,100% 100%,0 100%);justify-content:center;padding-left:40px;text-align:center}
.gem{position:absolute;width:86px;height:86px;transform:translate(-50%,-50%) rotate(45deg);border:4px solid var(--white);box-shadow:0 4px 10px rgba(0,0,0,.25)}
.gem svg{transform:rotate(-45deg);position:absolute;left:18px;top:18px}
.core{left:600px;top:2043px;width:220px;height:220px;transform:translate(-50%,-50%) rotate(45deg);background:var(--white);border:3px solid var(--navy);position:absolute}
.core-logo{left:505px;top:2026px;width:190px;justify-content:center;font-size:28px}

/* milestones */
.milestones{left:0;top:2323px;width:1200px;height:370px;background:var(--navy)}
.ms-title{left:0;top:2396px;width:1200px;text-align:center;font-size:31px;font-weight:800;color:var(--white)}
.ms-card{position:absolute;top:2467px;width:325px;height:153px;background:var(--grey-card);text-align:center;color:var(--navy)}
.ms-card .tab{position:absolute;left:50%;top:0;transform:translateX(-50%);width:66px;height:40px;background:var(--blue);clip-path:polygon(0 0,100% 0,100% 70%,50% 100%,0 70%);display:flex;align-items:flex-start;justify-content:center;padding-top:6px}
.ms-card .num{margin-top:52px;font-size:46px;font-weight:800;line-height:50px}
.ms-card .lbl{font-size:18px;font-weight:800;text-transform:uppercase;margin-top:4px}

/* platforms */
.pf-kicker{left:90px;top:2840px;font-size:22px;font-weight:800;color:var(--ink)}
.pf-title{left:90px;top:2870px;font-size:34px;line-height:47px;font-weight:800;color:var(--ink)}
.crane{left:696px;top:2794px;width:412px;height:229px;background:radial-gradient(ellipse 200px 60px at 250px 70px,rgba(200,200,200,.35),rgba(255,255,255,0) 75%)}
.tile{position:absolute;width:240px;height:100px;background:var(--white);box-shadow:0 2px 8px rgba(0,0,0,.18);display:flex;align-items:center;justify-content:center;font-size:26px;font-weight:700;color:var(--ink)}

/* bridge */
.bridge{left:0;top:3389px;width:1200px;height:412px;background:linear-gradient(90deg,#f28c1e 0%,#f39a1f 40%,#ee7325 75%,#ea5a21 100%);clip-path:polygon(0 0,360px 0,1200px 110px,1200px 412px,700px 412px,0 330px)}
.video{left:92px;top:3439px;width:487px;height:298px;background:var(--white);border:3px solid #2b2b2b;padding:14px 18px 14px 4px}
.video .frame{position:relative;width:100%;height:100%;
  background:
    radial-gradient(ellipse 60px 120px at 90px 200px,rgba(40,45,55,.7),rgba(40,45,55,0) 70%),
    radial-gradient(ellipse 60px 120px at 200px 210px,rgba(40,45,55,.7),rgba(40,45,55,0) 70%),
    radial-gradient(ellipse 60px 120px at 380px 210px,rgba(70,60,55,.6),rgba(70,60,55,0) 70%),
    linear-gradient(175deg,#dfe7ee 0%,#a9b8c6 35%,#6f7f8d 70%,#3f4a55 100%)}
.play{position:absolute;left:50%;top:50%;transform:translate(-50%,-50%);width:66px;height:66px;border-radius:50%;background:#e5161d;display:flex;align-items:center;justify-content:center}
.bridge-title{right:93px;top:3543px;text-align:right;font-size:33px;line-height:43px;font-weight:800;color:var(--white)}
.btn-gov{left:846px;top:3697px;width:261px;height:53px;background:var(--navy);color:var(--white);font-size:15px;font-weight:700;display:flex;align-items:center;justify-content:center}

/* contact */
.ct-title{left:92px;top:3850px;font-size:31px;font-weight:800;color:var(--ink)}
.ct-text{left:92px;width:420px;font-size:14.5px;line-height:25.5px;color:#555;letter-spacing:.2px}
.seal{left:92px;top:4065px;width:160px;height:130px;border-radius:50%;background:radial-gradient(circle,#f4c531 0%,#d9a81e 60%,#b7871a 100%)}
.field{position:absolute;border:1px solid #cfcfcf;background:var(--white);font-size:14px;color:#555;padding:18px 16px}
.submit{left:597px;top:4091px;width:182px;height:53px}

/* footer */
.footer{left:0;top:4232px;width:1200px;height:431px}
.ft-col{position:absolute;font-size:15px;color:var(--white);line-height:26px}
.ft-col a{color:var(--white);text-decoration:none;display:block;line-height:33px}
.ft-div{position:absolute;top:4351px;width:1px;height:247px;background:#3a4466}
.bottombar{left:0;top:4663px;width:1200px;height:54px;background:#ebebeb;display:flex;align-items:center;padding:0 92px;font-size:13px;color:#333}
.social{position:absolute;top:4675px;width:32px;height:32px;border-radius:50%;background:#2d2d2d}
.cert{position:absolute;top:4672px;background:#2d2d2d}
</style>
</head>
<body>

<div class="abs topbar">
  <span class="dot"><svg width="11" height="9" viewBox="0 0 11 9"><rect x=".5" y=".5" width="10" height="8" fill="none" stroke="#fff"/><path d="M.5 .5l5 4 5-4" fill="none" stroke="#fff"/></svg></span>
  marlene@brickwisely.com &nbsp;/&nbsp; support@brickwisely.com
  <span class="addr"><span class="dot"><svg width="10" height="13" viewBox="0 0 10 13"><path d="M5 12S1 7 1 4.5a4 4 0 018 0C9 7 5 12 5 12z" fill="#fff"/><circle cx="5" cy="4.5" r="1.5" fill="#f5a11c"/></svg></span>418 Fenwick Ave, Larkfield, KS 66210</span>
  <span class="login">Log in</span>
</div>

<div class="abs logo" style="left:88px;top:52px"><span class="mark"></span>BrickWisely</div>
<nav class="abs nav"><span>What We Offer</span><span>Portfolio</span><span>About</span><span>Podcast</span><span>Blogs</span></nav>
<div class="abs phone"><span class="dot"><svg width="16" height="16" viewBox="0 0 16 16"><path d="M3 1h3l1.5 4-2 1.2a9 9 0 004.3 4.3L11 8.5l4 1.5v3a2 2 0 01-2 2A12 12 0 011 3a2 2 0 012-2z" fill="#fff"/></svg></span>(555) 214-0387</div>

<div class="abs hero-visual" role="img" aria-label="Engineer in a hard hat looking over a city skyline with cranes, warm orange tint"></div>
<div class="abs hero-kicker">BUILD WITH THE ULTIMATE IN</div>
<h1 class="abs hero-title display">Construction<br>Technology</h1>
<ul class="abs hero-list">
  <li><svg width="13" height="11" viewBox="0 0 13 11"><path d="M1 6l4 4 7-9" fill="none" stroke="#1b1b1b" stroke-width="2"/></svg>Must solve problems not create them!</li>
  <li><svg width="13" height="11" viewBox="0 0 13 11"><path d="M1 6l4 4 7-9" fill="none" stroke="#1b1b1b" stroke-width="2"/></svg>Build 10x faster</li>
  <li><svg width="13" height="11" viewBox="0 0 13 11"><path d="M1 6l4 4 7-9" fill="none" stroke="#1b1b1b" stroke-width="2"/></svg>Build with actionable data</li>
  <li><svg width="13" height="11" viewBox="0 0 13 11"><path d="M1 6l4 4 7-9" fill="none" stroke="#1b1b1b" stroke-width="2"/></svg>Prepared for discovery in litigation</li>
  <li><svg width="13" height="11" viewBox="0 0 13 11"><path d="M1 6l4 4 7-9" fill="none" stroke="#1b1b1b" stroke-width="2"/></svg>Lower bond rate</li>
</ul>
<div class="abs btn-orange">CONTACT US</div>
<svg class="abs" style="left:0;top:630px" width="1200" height="100" viewBox="0 0 1200 100">
  <path d="M0 38 Q600 96 1200 22 L1200 100 L0 100Z" fill="#fff"/>
  <path d="M0 16 Q600 88 1200 8 L1200 24 Q600 100 0 40Z" fill="#f5a11c"/>
</svg>
<div class="abs dots" style="left:572px;top:698px"><i></i><i class="on"></i><i></i></div>

<div class="hex-wrap" style="left:95px;top:843px;width:286px;height:330px">
  <div class="hex"><div class="photo" role="img" aria-label="Portrait of co-founder Marlene R. Hadley" style="background:radial-gradient(ellipse 90px 110px at 50% 42%,#e9c3a5,rgba(233,195,165,0) 75%),linear-gradient(180deg,#7c8aa5 0%,#9aa3b6 40%,#3d4662 100%)"></div></div>
</div>
<div class="hex-wrap" style="left:302px;top:990px;width:244px;height:266px">
  <div class="hex"><div class="photo" role="img" aria-label="Portrait of co-founder Dorian Hadley" style="background:radial-gradient(ellipse 80px 95px at 50% 45%,#d9a98a,rgba(217,169,138,0) 75%),linear-gradient(180deg,#f0f0f0 0%,#e4e4e4 55%,#2e2f34 100%)"></div></div>
</div>
<svg class="abs" style="left:250px;top:860px" width="150" height="420" viewBox="0 0 150 420">
  <path d="M20 70 Q80 20 130 25" fill="none" stroke="#1b1b1b" stroke-width="2.5"/>
  <path d="M120 16l12 9-13 8" fill="none" stroke="#1b1b1b" stroke-width="2.5"/>
  <path d="M120 330 Q110 410 65 400" fill="none" stroke="#1b1b1b" stroke-width="2.5"/>
  <path d="M76 391l-12 9 12 8" fill="none" stroke="#1b1b1b" stroke-width="2.5"/>
</svg>
<div class="abs person" style="left:394px;top:864px">MARLENE R. HADLEY,<br><span>CEO &amp; FOUNDER</span></div>
<div class="abs person" style="left:100px;top:1238px;width:202px;text-align:right">DORIAN HADLEY<br><span>PRESIDENT &amp; FOUNDER</span></div>
<h2 class="abs about-title">ABOUT US</h2>
<p class="abs about-text" style="top:901px">Dorian and Marlene Hadley knew that there had to be a better way to do construction. The management of documents is daunting yet mandatory. The more technology that was brought to the project, the bigger the challenge becomes. Accurate information is the real key.</p>
<p class="abs about-text" style="top:1041px">Today's construction projects are too complex for traditional management techniques. Chaos cuts into bottom lines and into your sanity. The most successful construction management companies rely on software that can provide clear value by improving efficiency and ease of use.</p>
<div class="abs btn-dark" style="left:599px;top:1193px;width:181px;height:55px">Read More</div>

<div class="abs why-visual" role="img" aria-label="Two construction workers in hard hats reviewing plans on site, dark toned"></div>
<div class="abs why-panel"></div>
<h2 class="abs why-title heavy">Why we are the<br>best construction<br>management software</h2>

<div class="abs features"></div>
<div class="core"></div>
<div class="abs logo core-logo"><span class="mark"></span>BrickWisely</div>

<div class="ribbon left" style="left:262px;top:1803px;width:260px;background:#62b6de">Finish on time</div>
<div class="ribbon right" style="left:680px;top:1803px;width:254px;background:#62b6de">Bidding process</div>
<div class="ribbon left" style="left:174px;top:1900px;width:260px;background:#21a0d8">Stay on budget</div>
<div class="ribbon right" style="left:766px;top:1898px;width:260px;background:#21a0d8">Hold everyone<br>accountable</div>
<div class="ribbon left" style="left:92px;top:2012px;width:256px;background:#1d86b8">Project<br>information</div>
<div class="ribbon right" style="left:850px;top:2012px;width:257px;background:#1d86b8">Closeout<br>module</div>
<div class="ribbon left" style="left:110px;top:2125px;width:320px;background:#225a8f">Track (&amp; search)<br>documents</div>
<div class="ribbon right" style="left:768px;top:2125px;width:322px;background:#225a8f">Ease of use</div>
<div class="ribbon left" style="left:214px;top:2222px;width:304px;background:var(--navy-2)">Security</div>
<div class="ribbon right" style="left:684px;top:2222px;width:302px;background:var(--navy-2)">Customization</div>

<div class="gem" style="left:522px;top:1869px;background:#3aa7dc"><svg width="42" height="42" viewBox="0 0 42 42" fill="none" stroke="#fff" stroke-width="2"><circle cx="21" cy="23" r="14"/><path d="M21 14v9l6 4M17 5h8"/></svg></div>
<div class="gem" style="left:678px;top:1869px;background:#3aa7dc"><svg width="42" height="42" viewBox="0 0 42 42" fill="none" stroke="#fff" stroke-width="2"><rect x="4" y="6" width="10" height="8"/><rect x="28" y="28" width="10" height="8"/><circle cx="21" cy="21" r="5"/><path d="M14 10h12v6M28 32H16v-6"/></svg></div>
<div class="gem" style="left:430px;top:1964px;background:#1e9ad4"><svg width="42" height="42" viewBox="0 0 42 42" fill="none" stroke="#fff" stroke-width="2"><rect x="8" y="14" width="26" height="22" rx="3"/><path d="M15 14l6-8 6 8M21 18v14M25 21h-6a2.5 2.5 0 000 5h4a2.5 2.5 0 010 5h-6"/></svg></div>
<div class="gem" style="left:769px;top:1960px;background:#1e9ad4"><svg width="42" height="42" viewBox="0 0 42 42" fill="none" stroke="#fff" stroke-width="2"><rect x="9" y="5" width="24" height="32" rx="2"/><path d="M14 13h14M14 19h14M14 25h14M14 31h8"/></svg></div>
<div class="gem" style="left:344px;top:2046px;background:#1a80b4"><svg width="42" height="42" viewBox="0 0 42 42" fill="none" stroke="#fff" stroke-width="2"><circle cx="21" cy="21" r="7"/><path d="M21 5v6M21 31v6M5 21h6M31 21h6M10 10l4 4M28 28l4 4M32 10l-4 4M14 28l-4 4"/></svg></div>
<div class="gem" style="left:854px;top:2046px;background:#1a80b4"><svg width="42" height="42" viewBox="0 0 42 42" fill="none" stroke="#fff" stroke-width="2"><rect x="5" y="8" width="32" height="20" rx="2"/><path d="M16 36h10M21 28v8M12 20l5-5 4 4 8-7"/></svg></div>
<div class="gem" style="left:434px;top:2125px;background:#225a8f"><svg width="42" height="42" viewBox="0 0 42 42" fill="none" stroke="#fff" stroke-width="2"><path d="M24 30s-9-9-9-15a9 9 0 0118 0c0 6-9 15-9 15z"/><circle cx="24" cy="15" r="3"/><path d="M6 12v22h14" stroke-dasharray="3 3"/></svg></div>
<div class="gem" style="left:764px;top:2125px;background:#225a8f"><svg width="42" height="42" viewBox="0 0 42 42" fill="none" stroke="#fff" stroke-width="2"><circle cx="21" cy="11" r="5"/><path d="M8 34l5-12 8 4 8-4 5 12M13 22l-5-6M29 22l5-6"/></svg></div>
<div class="gem" style="left:522px;top:2220px;background:var(--navy-2)"><svg width="42" height="42" viewBox="0 0 42 42" fill="none" stroke="#fff" stroke-width="2"><path d="M21 4l14 5v10c0 9-6 15-14 19C13 34 7 28 7 19V9z"/><path d="M14 21l5 5 9-10"/></svg></div>
<div class="gem" style="left:678px;top:2220px;background:var(--navy-2)"><svg width="42" height="42" viewBox="0 0 42 42" fill="none" stroke="#fff" stroke-width="2"><rect x="6" y="6" width="30" height="30" rx="2"/><path d="M6 13h30"/><circle cx="21" cy="25" r="5"/><path d="M21 17v3M21 30v3M13 25h3M26 25h3"/></svg></div>

<div class="abs milestones"></div>
<h2 class="abs ms-title">MILESTONES</h2>
<div class="ms-card" style="left:92px">
  <div class="tab"><svg width="22" height="20" viewBox="0 0 22 20" fill="none" stroke="#fff" stroke-width="1.6"><rect x="1" y="4" width="20" height="15"/><path d="M1 8h20M6 1v5M16 1v5"/></svg></div>
  <div class="num">16</div><div class="lbl">Years in business</div>
</div>
<div class="ms-card" style="left:438px">
  <div class="tab"><svg width="22" height="20" viewBox="0 0 22 20" fill="none" stroke="#fff" stroke-width="1.6"><rect x="1" y="1" width="20" height="18"/><circle cx="11" cy="10" r="4"/></svg></div>
  <div class="num">+ 2K</div><div class="lbl">Projects completed</div>
</div>
<div class="ms-card" style="left:782px">
  <div class="tab"><svg width="22" height="20" viewBox="0 0 22 20" fill="none" stroke="#fff" stroke-width="1.6"><rect x="1" y="1" width="20" height="18"/><path d="M4 15l5-5 4 3 6-7"/></svg></div>
  <div class="num">$ 23B</div><div class="lbl">Construction value</div>
</div>

<div class="abs crane" role="img" aria-label="Faint line drawing of a tower crane"></div>
<div class="abs pf-kicker">WE IMPROVE ALL</div>
<h2 class="abs pf-title">CONSTRUCTION MANAGEMENT<br>SOFTWARE PLATFORMS</h2>
<div class="tile" style="left:92px;top:3041px">Stackline</div>
<div class="tile" style="left:348px;top:3041px">Ducton</div>
<div class="tile" style="left:606px;top:3041px">Modelvault</div>
<div class="tile" style="left:863px;top:3041px">Terrabuild</div>
<div class="tile" style="left:92px;top:3157px">Siteroster</div>
<div class="tile" style="left:348px;top:3157px">Ledgerpine</div>
<div class="tile" style="left:606px;top:3157px">Corvant</div>
<div class="tile" style="left:863px;top:3157px">Buildtally</div>
<div class="abs dots" style="left:574px;top:3314px"><i class="on"></i><i></i><i></i></div>

<div class="abs bridge"></div>
<div class="abs video">
  <div class="frame" role="img" aria-label="Business people walking outside a glass office building">
    <div class="play"><svg width="18" height="20" viewBox="0 0 18 20"><path d="M2 1l15 9-15 9z" fill="#fff"/></svg></div>
  </div>
</div>
<h2 class="abs bridge-title">BRIDGE THE GAP IN<br>PROJECT MANAGEMENT<br>SOFTWARE</h2>
<div class="abs btn-gov">GOVERNMENT PROJECTS</div>

<h2 class="abs ct-title">CONTACT US</h2>
<p class="abs ct-text" style="top:3899px">Using our array of services, you can finally alleviate the stress of managing large construction projects. Find out how BrickWisely solves</p>
<p class="abs ct-text" style="top:3989px">the largest problems in project management and how you can benefit.</p>
<div class="abs seal" role="img" aria-label="Litigation protection guarantee seal"></div>
<div class="field" style="left:595px;top:3856px;width:250px;height:57px">Name</div>
<div class="field" style="left:856px;top:3856px;width:251px;height:57px">Email</div>
<div class="field" style="left:595px;top:3930px;width:512px;height:148px">Message</div>
<div class="abs btn-dark submit">Submit Now</div>

<svg class="abs footer" viewBox="0 0 1200 431">
  <path d="M0 90 L600 0 L1200 90 L1200 431 L0 431Z" fill="#f5a11c"/>
  <path d="M0 112 L600 14 L1200 112 L1200 431 L0 431Z" fill="#0a1430"/>
</svg>
<div class="abs logo" style="left:92px;top:4392px;color:#cfd3dd;font-size:28px"><span class="mark"></span>BrickWisely</div>
<div class="ft-col" style="left:92px;top:4462px">
  <div style="display:flex;align-items:center;gap:10px"><svg width="14" height="11" viewBox="0 0 14 11"><rect x=".5" y=".5" width="13" height="10" fill="#f5a11c"/><path d="M.5 .5l6.5 5 6.5-5" fill="none" stroke="#0a1430"/></svg>Email:</div>
  <div style="padding-left:26px">marlene@brickwisely.com<br>support@brickwisely.com</div>
</div>
<div class="ft-div" style="left:376px"></div>
<div class="ft-col" style="left:418px;top:4378px">
  <div style="display:flex;align-items:center;gap:10px"><svg width="10" height="13" viewBox="0 0 10 13"><path d="M5 12S1 7 1 4.5a4 4 0 018 0C9 7 5 12 5 12z" fill="#f5a11c"/></svg>Location:</div>
  <div style="padding-left:20px">418 Fenwick Ave<br>Larkfield, KS 66210</div>
  <div style="display:flex;align-items:center;gap:10px;margin-top:22px"><svg width="12" height="12" viewBox="0 0 16 16"><path d="M3 1h3l1.5 4-2 1.2a9 9 0 004.3 4.3L11 8.5l4 1.5v3a2 2 0 01-2 2A12 12 0 011 3a2 2 0 012-2z" fill="#f5a11c"/></svg>Phone:</div>
  <div style="padding-left:20px">(555) 214-0387</div>
</div>
<div class="ft-div" style="left:634px"></div>
<div class="ft-col" style="left:680px;top:4374px">
  <a>Owners / Shareholders</a><a>Contractors</a><a>Construction Lawyers</a><a>Finance</a>
</div>
<div class="ft-div" style="left:900px"></div>
<div class="ft-col" style="left:951px;top:4374px">
  <a>Privacy policy</a><a>Terms &amp; Conditions</a><a>Disclaimer</a>
</div>

<div class="abs bottombar">©2022&nbsp;<strong>BrickWisely.</strong>&nbsp;All Rights Reserved</div>
<span class="social" style="left:524px"></span>
<span class="social" style="left:563px"></span>
<span class="social" style="left:603px"></span>
<span class="social" style="left:644px"></span>
<span class="cert" style="left:806px;width:56px;height:36px;border-radius:50%;background:#2a6fb8"></span>
<span class="cert" style="left:870px;width:130px;height:34px;border-radius:3px;background:#1f3e7a"></span>
<span class="cert" style="left:1010px;width:42px;height:42px;top:4669px;border-radius:50%"></span>
<span class="cert" style="left:1060px;width:42px;height:42px;top:4669px;border-radius:50%"></span>

</body>
</html>
```